Stationary for Korvex
Korvexx
Project: Stationary for Korvex
Stationary for Korvex - Telecommunications
Korvex
R Peter Hallam
CEO
5678 East Millbrook Avenue #C Harlow Springs, UT 84000
801-555-0137 Main
801-555-0152 Direct
Peter@korvexx.example
www.korvexx.example
Want the front to be clean and simple with the AI file of our logo that I sent you with MAYBE the main number and web address located on the front in a small fashion.
This is where I want the bulk of the information presented in an appealing way.

```html
<!DOCTYPE html>
<html lang="en">
<head>
<meta charset="utf-8">
<title>Stationery for Korvex</title>
<link rel="stylesheet" href="https://fonts.googleapis.com/css2?family=Michroma&family=Montserrat:wght@300;400&display=swap">
<style>
  :root {
    --backdrop: #5b3021;
    --card: #0b0b0b;
    --card-edge: #3a3a3a;
    --ink: #e6e6e6;
    --ink-soft: #9a9a9a;
    --accent: #c8171d;
    --rule: #4a4a4a;
  }
  html, body {
    margin: 0;
    padding: 0;
    width: 1200px;
    height: 802px;
    overflow: hidden;
    background: var(--backdrop);
  }
  .canvas {
    position: relative;
    width: 1200px;
    height: 802px;
  }
  .card {
    position: absolute;
    width: 460px;
    height: 266px;
    background: var(--card);
    border: 1px solid var(--card-edge);
    border-radius: 16px;
    box-sizing: border-box;
    overflow: hidden;
  }
  .card--back { left: 122px; top: 116px; }
  .card--front { left: 510px; top: 416px; }

  .brand {
    position: absolute;
    text-align: center;
    font-family: "Michroma", sans-serif;
    color: var(--ink);
  }
  .brand__mark {
    display: block;
    margin: 0 auto;
    border-radius: 50%;
    background: var(--accent);
  }
  .brand__name {
    display: block;
    letter-spacing: 3px;
    text-transform: uppercase;
    white-space: nowrap;
  }
  .brand__tagline,
  .brand__web {
    display: block;
    font-family: "Montserrat", sans-serif;
    font-weight: 300;
    color: var(--ink-soft);
    text-transform: uppercase;
    white-space: nowrap;
  }

  .card--back .brand { left: 10px; top: 34px; width: 212px; }
  .card--back .brand__mark { width: 80px; height: 80px; }
  .card--back .brand__name { font-size: 24px; margin-top: 40px; }
  .card--back .brand__tagline { font-size: 7px; letter-spacing: 1.4px; margin-top: 6px; }
  .card--back .brand__web { font-size: 7px; letter-spacing: 2px; margin-top: 6px; }

  .divider {
    position: absolute;
    left: 232px;
    top: 38px;
    width: 1px;
    height: 196px;
    background: var(--rule);
  }

  .contact {
    position: absolute;
    left: 246px;
    top: 56px;
    right: 0;
    font-family: "Montserrat", sans-serif;
    font-weight: 300;
    color: var(--ink-soft);
    text-transform: uppercase;
  }
  .contact__name {
    font-size: 11px;
    letter-spacing: 1.6px;
    color: var(--ink);
    margin: 0;
    white-space: nowrap;
  }
  .contact__role { color: var(--ink-soft); }
  .contact__flag {
    position: absolute;
    right: 0;
    top: 2px;
    width: 34px;
    height: 11px;
    background: var(--accent);
  }
  .contact__block {
    margin: 0;
    font-size: 6.6px;
    line-height: 12px;
    letter-spacing: 1.2px;
    white-space: nowrap;
  }
  .contact__address { margin-top: 26px; }
  .contact__phones { margin-top: 12px; }
  .contact__web { margin-top: 20px; }

  .card--front .brand { left: 0; right: 0; top: 34px; }
  .card--front .brand__mark { width: 86px; height: 86px; }
  .card--front .brand__name { font-size: 27px; margin-top: 22px; }
  .card--front .brand__tagline { font-size: 7.5px; letter-spacing: 2.8px; margin-top: 6px; }
  .card--front .brand__web { font-size: 7px; letter-spacing: 2.2px; margin-top: 6px; }
</style>
</head>
<body>
<main class="canvas">

  <section class="card card--back" aria-label="Business card, information side">
    <div class="brand">
      <span class="brand__mark" aria-hidden="true"></span>
      <span class="brand__name">Korvexx</span>
      <span class="brand__tagline">Communications made Korvex</span>
      <span class="brand__web">www.korvexx.example</span>
    </div>

    <div class="divider" aria-hidden="true"></div>

    <div class="contact">
      <p class="contact__name">R Peter Hallam <span class="contact__role">| CEO</span></p>
      <span class="contact__flag" aria-hidden="true"></span>
      <p class="contact__block contact__address">
        5678 East Millbrook Avenue #C<br>
        Harlow Springs, UT 84000
      </p>
      <p class="contact__block contact__phones">
        801-555-0137 Main<br>
        801-555-0152 Direct<br>
        Peter@korvexx.example
      </p>
      <p class="contact__block contact__web">www.korvexx.example</p>
    </div>
  </section>

  <section class="card card--front" aria-label="Business card, logo side">
    <div class="brand">
      <span class="brand__mark" aria-hidden="true"></span>
      <span class="brand__name">Korvexx</span>
      <span class="brand__tagline">Communications made Korvex</span>
      <span class="brand__web">www.korvexx.example</span>
    </div>
  </section>

</main>
</body>
</html>
```